RTV CRAFTED

building services
decks
pergola
renovation
extensions
general building

Target Market(s)

middle to upper class

Industry/Entity Type

building

Contact Information for Business Card

my details 0427839152 pkharlow47@mailvane.net BLD574926

Font styles to use
Serif

Colors
00AB8E
00BBA5
67D7C9
C6EFE9
E9F9F6

Requirements
Must have
• logo on the front and details on the back
Nice to have
• sharp and clean lines

```html
<!DOCTYPE html>
<html lang="en">
<head>
<meta charset="utf-8">
<title>RTV Crafted – Business Card</title>
<link href="https://fonts.googleapis.com/css2?family=Libre+Caslon+Text:wght@400&family=Montserrat:wght@500;600;700&display=swap" rel="stylesheet">
<style>
  :root {
    --teal: #00AB8E;
    --teal-bright: #00BBA5;
    --charcoal: #434345;
    --ink: #3a3a3c;
    --paper: #ffffff;
    --backdrop: #e4e5e6;
    --rule: #c9c9c9;
  }
  * { margin: 0; padding: 0; box-sizing: border-box; }
  html, body {
    width: 842px; height: 1200px; overflow: hidden;
    background: var(--backdrop);
    font-family: "Montserrat", Arial, sans-serif;
  }
  .sheet {
    position: relative; width: 842px; height: 1200px;
    display: flex; flex-direction: column; align-items: center; justify-content: center; gap: 110px;
  }
  .card {
    position: relative; width: 630px; height: 360px; border-radius: 22px;
    box-shadow: 0 10px 30px rgba(0,0,0,0.18);
    overflow: hidden;
  }
  /* Front: details */
  .card--details { background: var(--paper); display: flex; align-items: center; }
  .brand {
    width: 290px; display: flex; align-items: center; justify-content: center; gap: 10px;
  }
  .brand__mark { width: 12px; height: 12px; background: var(--teal); flex: none; }
  .brand__name {
    font-family: "Libre Caslon Text", Georgia, serif;
    font-weight: 400; font-size: 30px; letter-spacing: 1px; color: var(--ink); white-space: nowrap;
  }
  .divider { width: 1px; height: 210px; background: var(--rule); flex: none; }
  .details { padding-left: 38px; }
  .details__name { font-weight: 600; font-size: 23px; color: var(--ink); letter-spacing: 0.5px; line-height: 1.1; }
  .details__role { font-weight: 600; font-size: 15px; color: var(--teal); margin-bottom: 18px; }
  .details__line {
    display: flex; align-items: center; gap: 12px; white-space: nowrap;
    font-weight: 500; font-size: 14px; color: var(--ink); margin-bottom: 7px;
  }
  .details__line svg { width: 14px; height: 14px; flex: none; }
  /* Back: brand */
  .card--brand {
    background: var(--charcoal);
    display: flex; flex-direction: column; align-items: center; justify-content: center; gap: 46px;
  }
  .card--brand .brand { width: auto; }
  .card--brand .brand__name { color: var(--paper); font-size: 48px; }
  .ribbon { width: 360px; height: 40px; display: block; }
  .ribbon text {
    font-family: "Montserrat", Arial, sans-serif; font-weight: 700; font-size: 14px;
    letter-spacing: 5px; fill: var(--paper);
  }
</style>
</head>
<body>
<main class="sheet">

  <section class="card card--details" aria-label="Card front with contact details">
    <div class="brand">
      <span class="brand__mark"></span>
      <span class="brand__name">RTV CRAFTED</span>
    </div>
    <div class="divider"></div>
    <div class="details">
      <p class="details__name">PETER HARLOW</p>
      <p class="details__role">Founder</p>
      <p class="details__line">
        <svg viewBox="0 0 14 14" aria-hidden="true"><rect x="3" y="1" width="8" height="12" rx="1.5" fill="none" stroke="var(--teal)" stroke-width="1.3"/><line x1="6" y1="11" x2="8" y2="11" stroke="var(--teal)" stroke-width="1.2"/></svg>
        0427839152
      </p>
      <p class="details__line">
        <svg viewBox="0 0 14 14" aria-hidden="true"><rect x="1" y="3" width="12" height="8.5" rx="1" fill="var(--teal)"/><polyline points="1.5,3.6 7,8 12.5,3.6" fill="none" stroke="#fff" stroke-width="1.1"/></svg>
        pkharlow47@mailvane.net
      </p>
      <p class="details__line">
        <svg viewBox="0 0 14 14" aria-hidden="true"><g fill="none" stroke="var(--teal)" stroke-width="1.1"><circle cx="7" cy="7" r="5.6"/><ellipse cx="7" cy="7" rx="2.4" ry="5.6"/><line x1="1.4" y1="7" x2="12.6" y2="7"/></g></svg>
        www.RTVcrafted.com
      </p>
      <p class="details__line">
        <svg viewBox="0 0 14 14" aria-hidden="true"><g fill="none" stroke="var(--teal)" stroke-width="1.2"><rect x="1" y="2.5" width="12" height="9" rx="1"/><line x1="3.5" y1="5.5" x2="10.5" y2="5.5"/><line x1="3.5" y1="8.5" x2="8" y2="8.5"/></g></svg>
        Lic. BLD574926
      </p>
    </div>
  </section>

  <section class="card card--brand" aria-label="Card back with brand name">
    <div class="brand">
      <span class="brand__mark"></span>
      <span class="brand__name">RTV CRAFTED</span>
    </div>
    <svg class="ribbon" viewBox="0 0 360 40" aria-hidden="true">
      <polygon points="0,4 360,4 344,20 360,36 0,36 16,20" fill="var(--teal)"/>
      <text x="180" y="25" text-anchor="middle">www.RTVcrafted.com</text>
    </svg>
  </section>

</main>
</body>
</html>
```